I need the front of this bottle designed for and calendula and tallow lotion. the dimenstions are 236mm by 84 mm the Minimalists design if you choose a graphic should be very minimal and high end I don thave a logo. My company name is The Bright Seed Co, If you want to ceate a logo using the The Bright Seed Co ( letters only) That would be ok

```html
<!DOCTYPE html>
<html lang="en">
<head>
<meta charset="UTF-8">
<title>The Bright Seed Co – Calendula &amp; Tallow Lotion Label</title>
<link rel="stylesheet" href="https://fonts.googleapis.com/css2?family=Bebas+Neue&family=Marcellus&display=swap">
<style>
  :root {
    --label-sand: #ab9a85;
    --ink: #201e1f;
  }
  html, body {
    margin: 0;
    padding: 0;
    width: 1200px;
    height: 427px;
    overflow: hidden;
    background: var(--label-sand);
  }
  .label {
    position: relative;
    width: 1200px;
    height: 427px;
    background: var(--label-sand);
    color: var(--ink);
  }
  .brand-name {
    position: absolute;
    top: 56px;
    left: 0;
    width: 100%;
    text-align: center;
    font-family: "Marcellus", serif;
    font-size: 30px;
    line-height: 1;
    letter-spacing: 4px;
    margin: 0;
    font-weight: 400;
  }
  .product-title {
    position: absolute;
    top: 0;
    left: 0;
    width: 1200px;
    height: 427px;
  }
  .product-title .rule { fill: var(--ink); }
  .product-title .title-line {
    font-family: "Bebas Neue", sans-serif;
    font-size: 86px;
    fill: var(--ink);
  }
  .volume {
    position: absolute;
    top: 350px;
    left: 0;
    width: 100%;
    text-align: center;
    font-family: "Marcellus", serif;
    font-size: 40px;
    line-height: 1;
    margin: 0;
  }
</style>
</head>
<body>
  <main class="label">
    <p class="brand-name">THE BRIGHT SEED CO</p>

    <svg class="product-title" viewBox="0 0 1200 427" role="heading" aria-level="1" aria-label="Calendula &amp; Tallow Lotion">
      <rect class="rule rule--top" x="391" y="145" width="418" height="7"/>
      <text class="title-line" x="399" y="227" textLength="360" lengthAdjust="spacingAndGlyphs">CALENDULA &amp;</text>
      <text class="title-line" x="396" y="303" textLength="409" lengthAdjust="spacingAndGlyphs">TALLOW LOTION</text>
      <rect class="rule rule--bottom" x="391" y="320" width="418" height="7"/>
    </svg>

    <p class="volume">500 ml</p>
  </main>
</body>
</html>
```